Guarenteed! - Homepage Website Design - Coding not required- Winner to complete further pages

Hi all,

We're looking at redesigning our current website with a few adjustments to other pages but the main adjustments will be on the homepage which is what this design request is for. Please note : any of these ideas can be changed if you have something particularly different / special in mind etc.

P.S Coding is not required, just a design.

- Our website -

Our website is simply a price comparison website that allows customers to find companies within their area at the best price. The products available are mostly related to the vehicle trade and all refer to vinyl. This includes the likes of vehicle window tint, vehicle colour change vehicle wrap, vehicle signage as well as other cosmetic vinyl modifications. We allow the customer to search for their product within their chosen area and receive a list of companies who supply their product within that area. From here they can compare prices and view further details on the company.

- What we're looking to do -

We're looking first of all to adjust how the website homepage is displayed, this includes adding images and adjusting the colours that are explained below:

First of all, we look to spread out each of the 12 products (which can be seen on the website as it stands) and add an image to each of the products (all being spaced out as shown in our sketch)

We've been told the website looks too busy so we're thinking if we adjust the colours to more simplier neutral colours as well as the main focus of the website being on the 12 images, that would be great.

- Logo + Banner -

Logo to remain top left although banner may be removed / adjusted to make simplier.

- Colours -

Adjustments - Colours shades
We want the website to still look exciting but simplify the colours. Needs to be kept up to date with the colours / textures etc (bright colours to highlight keypoints)
We're still looking to use either blue or orange or maybe both to highlight these keypoints but the main website to be light colours and maybe even black on white background. The entire homepage can be adjusted colour wise if you feel it fits into your theme including menu bars, banners etc. The key is to get this right with being not too overpowering with the colours but still look interesting and up to date.

- 1 - 4 steps banner - (text may change)

This sits just under the logo and explains to the user how easy the website is to use and the steps they need to take. This may change to a 1 - 5 steps but we're looking to have this designed once the overall colours / theme of the website is sorted.

- 12 images - 4 x 3

This is the main focus of the website and will be the main focus of what the customer sees first of all. This will be where they select their product and then underneath, enter their postcode and distance they would like to search within. As explained further up, we have some of the product images available so if you can where possible add these to the design and then duplicate the images on those we currently don't have available.

- 12 Images -Titles -

These titles will be in this order from left to right and etc

- Colour Change Wrap
- Printed Vehicle Wrap
- Window Tint
- Headlight Tint
- Vehicle Signage
- Shop Signage
- Roof Vinyl Wrap
- Bonnet Vinyl Wrap
- Carbon Fibre Vinyl
- Stickerbomb Vinyl
- Clear Protective Vinyl
- Wheel Refurb

Text to be quite large, centered and with the o to the left of the title. Short titles like 'Window Tint' should fit on one line in the middle of the box where as titles such as ' Stickerbomb Vinyl Wrap' should have the 'Stickerbomb Vinyl' on the first line with the 'Wrap' on the line below. The background of this text is up to experient, might be worth just a simple colour or it might be worth using a bright blue or orange to keep in with the theme of the logo etc.

These will also have the circle tick box to the left of the title (as on the current website) where the customer clicks to select the product they have available.
We were also thinking that if when the customer ticks the circle on their selected box, the box is highlighted in some way to show this.

- Search Block -

This will appear under the 12 images and allows the customer to input their postcode and distance for the search criteria. Colours on this can of course be adjusted to keep in theme with the website.

- Under the 12 Images -

- Block underneath the 12 images and search block -

To the left will be some key bullet points about the website - maybe 4 or 5 with a green tick to the left of this. Background colour will probably be best to be a light colour, possibly grey.

Then to the right of this will appear 4 images, 2 before and 2 after when applying these products. Images to be used aren't fully decided on and we would like this stage of the design left to the end when the rest of the theme etc have been decided on.

Attached images are as follows :
- How the website looks as it stands
- The fold line on the website (obviously important)
- Our rough sketch of how we'd like the website homepage to look.
- We have 7 of the images ready that are all attached in this one file. Please duplicate the images on those that currently don't have the image available.

We will also be requesting a website developer to put this into action if our current designer falls through so please feel free to contact us if potentially interested.

The layout can change if you can think of something particular different / unique that works with this design. The main idea is to not only get the 12 products on view to the viewers but also the keypoints and before and after images.

Any questions, please ask away as we're bound to have forgotten a few things.

Thanks and good luck!

Hi all, keep the designs coming.

We haven't quite seen that extra special design we're after. As stated, we're after something fairly simple to suit the youth as well as the middle aged but we're also after something that bit special.

Colours to concentrate on are still and orange etc although feel free to use other colours if you have anything special in mind.

Please experience and we'll give you our honest feedback.

Many thanks all and good luck!

Hi all, this is a message to all the designers.

Some good designs coming in but we're still after that something special for the website design. Keep the designs coming and please feel free to experiment with the design colours, layout etc.

The basic principle of the website needs to remain regarding the 12 products, search within block and 4 steps all appearing on the homepage.

The 4 steps seems to work best when it's got text as well as some simple images next to this.

A variation with the product titles with how to display this, some designers have gone with a simple white background whereas others have gone with colours. Please experiment here and where possible, add a contract / texture to the colour. Please remember the product titles needs to be clear, centured and with the circle tick box to the left of it. 

We're after a fairly simple design although we need it to look 21st century, up to date as well as interesting. The key points straight away are the 4 steps as well as the 12 products so try to guide the viewer to these areas a little.

White background behind the 12 images seems to be a much, although a light colour could possibly work.

The keypoints underneath these 12 products are too very important as it outlines what we do etc. Tick colour can vary.

Next to these keypoints will be the 'before' and 'after' images, these images needs to be fairly small and ensure there is white background around the image itself.

Good luck all and any questions, feel free to ask away.

Thanks!

Hi,

 Thank you for your time and effort with these designs, we are very nearly there with the design but we've thought of something that may work for the homepage. A curved arrow from step 1 pointing to the products, this may or may not work but feel free to give it a go.

Many thanks,

Thank you to everyone for your time and efforts with the design. It's hugely appreciated so thank you all once again.

Wish you all the luck in the future.

```html
<!DOCTYPE html>
<html lang="en">
<head>
<meta charset="utf-8">
<title>Wrap Finder Hub – Find and Compare Vinyl Installers</title>
<link href="https://fonts.googleapis.com/css2?family=Arimo:ital,wght@0,400;0,700;1,400;1,700&family=Roboto+Condensed:wght@700&display=swap" rel="stylesheet">
<style>
:root{
  --page:#e6e6e6;
  --white:#ffffff;
  --ink:#1b1b1b;
  --muted:#333333;
  --orange:#f7931e;
  --orange-light:#fbab4c;
  --blue-dark:#3b5795;
  --blue-mid:#5673b0;
  --blue-light:#7089c2;
  --black:#0b0b0b;
  --grey-btn:#8a8a8a;
}
*{box-sizing:border-box;margin:0;padding:0}
html,body{width:1152px;height:1200px;overflow:hidden}
body{background:var(--page);font-family:"Arimo",Arial,sans-serif;color:var(--ink);position:relative}
.column{position:absolute;left:52px;top:0;width:1040px;height:1200px;background:var(--white);box-shadow:0 0 14px rgba(0,0,0,.25)}
.brand{position:absolute;left:82px;top:46px;display:flex;align-items:center;gap:12px}
.brand-dot{width:40px;height:40px;border-radius:50%;background:var(--orange)}
.brand-name{font-weight:700;font-size:34px;color:#3a3a3a;letter-spacing:.5px}
.nav{position:absolute;left:537px;top:104px;display:flex;font-size:13px;color:#222;list-style:none}
.nav li{padding:0 14px;border-left:1px solid #444;line-height:13px}
.nav li:first-child{border-left:0;padding-left:0;color:var(--orange)}
.nav li:last-child{padding-right:0}
.steps-band{position:absolute;left:0;top:138px;width:1152px;height:160px;
  background:radial-gradient(ellipse at 55% 45%,var(--blue-light) 0%,var(--blue-mid) 45%,var(--blue-dark) 100%);color:var(--white)}
.steps-title{position:absolute;left:72px;top:28px;font-style:italic;font-size:22px}
.step{position:absolute;top:76px;display:flex;align-items:center;gap:8px}
.step-num{width:50px;height:50px;border-radius:50%;background:var(--orange);border:3px solid #fff;
  display:flex;align-items:center;justify-content:center;font-weight:700;font-size:34px;box-shadow:0 2px 4px rgba(0,0,0,.3)}
.step-text{font-weight:700;font-style:italic;font-size:20px;line-height:24px}
.divider{position:absolute;left:52px;top:298px;width:1040px;height:5px;background:var(--black)}
.products{position:absolute;left:79px;top:343px;display:grid;grid-template-columns:221px 220px 221px 221px;column-gap:32px;row-gap:43px}
.products .tile:nth-child(4n+2){margin-left:-0px}
.tile{width:221px;height:157px;border-top:3px solid var(--black);position:relative;background:#ececec}
.tile-photo{height:103px}
.photo-van{background:linear-gradient(180deg,#6fa4d8 0%,#cfe2f2 38%,#f3f3f3 55%,#7aa43a 78%,#3f6d1e 100%)}
.photo-car{background:linear-gradient(160deg,#ececec 0%,#ececec 30%,#4bb84a 45%,#2f8f2e 60%,#ececec 70%,#3ea93c 85%,#ececec 100%)}
.tile-bar{position:absolute;left:0;bottom:0;width:100%;height:51px;
  background:linear-gradient(120deg,var(--orange) 0 64%,var(--orange-light) 64% 100%);color:var(--white);padding:5px 0 0 13px}
.tile-bar::before{content:"";position:absolute;left:105px;top:-12px;border:12px solid transparent;border-top:0;border-bottom-color:var(--orange)}
.tile-small{font-size:17px;line-height:18px;display:block}
.tile-big{font-size:23px;line-height:25px;display:block}
.tile-go{position:absolute;right:12px;top:14px;width:23px;height:23px}
.search-band{position:absolute;left:52px;top:937px;width:1040px;height:40px;
  background:linear-gradient(100deg,var(--blue-dark) 0 56%,var(--blue-mid) 56% 100%);color:var(--white);display:flex;align-items:center;box-shadow:0 3px 4px rgba(0,0,0,.2)}
.search-lead{margin-left:127px;font-style:italic;font-size:16px}
.search-label{font-family:"Roboto Condensed",Arial Narrow,sans-serif;font-size:17px;margin-left:14px}
.search-field{width:112px;height:22px;background:#fff;border:1px solid #bbb;margin-left:6px;font-size:9px;color:#aaa;padding:5px 5px;font-family:"Arimo",sans-serif}
.search-field.wide{margin-left:10px;width:114px}
.search-button{margin-left:14px;height:24px;padding:0 9px;background:linear-gradient(#9a9a9a,#777);color:#fff;font-family:"Roboto Condensed",sans-serif;font-size:15px;line-height:24px;border:1px solid #666}
.help-title{position:absolute;left:87px;top:998px;font-style:italic;font-size:29px}
.help-list{position:absolute;left:110px;top:1052px;list-style:none}
.help-list li{position:relative;font-style:italic;font-size:19px;line-height:36px;padding-left:24px}
.help-list li::before{content:"";position:absolute;left:0;top:11px;border-left:13px solid var(--orange);border-top:7px solid transparent;border-bottom:7px solid transparent}
.compare{position:absolute;top:1017px;width:290px;height:132px;background:var(--white);box-shadow:0 0 3px rgba(0,0,0,.35)}
.compare-before{left:472px}
.compare-after{left:778px}
.compare-photo{height:101px;background:linear-gradient(105deg,var(--orange) 0 30%,#d8d8d8 55%,#b8bcc0 80%,#9fa4a8 100%)}
.compare-label{position:absolute;left:0;bottom:0;width:100%;height:31px;background:var(--black);color:#fff;font-size:16px;padding:7px 0 0 14px;letter-spacing:.5px}
.compare-tag{position:absolute;left:10px;top:6px;color:#fff;line-height:1}
.compare-tag span{display:block;font-size:24px}
.compare-tag strong{display:block;font-weight:400;font-size:38px}
.footer-bar{position:absolute;left:52px;top:1192px;width:1040px;height:8px;background:var(--black)}
</style>
</head>
<body>
<div class="column"></div>

<header>
  <div class="brand"><span class="brand-dot"></span><span class="brand-name">WRAP FINDER HUB</span></div>
  <ul class="nav">
    <li>HOME</li><li>ABOUT US</li><li>CONTACT US</li><li>BLOG</li><li>LIST YOUR COMPANY</li>
  </ul>
</header>

<section class="steps-band">
  <p class="steps-title">Compare Professional Installers Today With These Four Easy Steps...</p>
  <div class="step" style="left:86px"><span class="step-num">1</span><span class="step-text">Select Chosen<br>Product</span></div>
  <div class="step" style="left:305px"><span class="step-num">2</span><span class="step-text">Input Postcode<br>Distance &amp; Search</span></div>
  <div class="step" style="left:568px"><span class="step-num">3</span><span class="step-text">Compare Companies<br>&amp; Prices</span></div>
  <div class="step" style="left:851px"><span class="step-num">4</span><span class="step-text">Contact Chosen<br>Company</span></div>
</section>
<div class="divider"></div>

<main class="products">
  <!-- row 1 -->
  <div class="tile"><div class="tile-photo photo-van" role="img" aria-label="White van with colour change wrap"></div><div class="tile-bar"><span class="tile-small">COLOR CHANGE</span><span class="tile-big">WRAP</span><svg class="tile-go" viewBox="0 0 24 24"><circle cx="12" cy="12" r="12" fill="#fff"/><path d="M9 6l8 6-8 6z" fill="#111"/></svg></div></div>
  <div class="tile"><div class="tile-photo photo-van" role="img" aria-label="Van with printed vehicle wrap"></div><div class="tile-bar"><span class="tile-small">PRINTED VEHICLE</span><span class="tile-big">WRAP</span><svg class="tile-go" viewBox="0 0 24 24"><circle cx="12" cy="12" r="12" fill="#fff"/><path d="M9 6l8 6-8 6z" fill="#111"/></svg></div></div>
  <div class="tile"><div class="tile-photo photo-car" role="img" aria-label="Two green hatchbacks with tinted windows"></div><div class="tile-bar"><span class="tile-small">WINDOW</span><span class="tile-big">TINT</span><svg class="tile-go" viewBox="0 0 24 24"><circle cx="12" cy="12" r="12" fill="#fff"/><path d="M9 6l8 6-8 6z" fill="#111"/></svg></div></div>
  <div class="tile"><div class="tile-photo photo-car" role="img" aria-label="Two green hatchbacks with tinted headlights"></div><div class="tile-bar"><span class="tile-small">HEADLIGHT</span><span class="tile-big">TINTING</span><svg class="tile-go" viewBox="0 0 24 24"><circle cx="12" cy="12" r="12" fill="#fff"/><path d="M9 6l8 6-8 6z" fill="#111"/></svg></div></div>
  <!-- row 2 -->
  <div class="tile"><div class="tile-photo photo-van" role="img" aria-label="White van with colour change wrap"></div><div class="tile-bar"><span class="tile-small">COLOR CHANGE</span><span class="tile-big">WRAP</span><svg class="tile-go" viewBox="0 0 24 24"><circle cx="12" cy="12" r="12" fill="#fff"/><path d="M9 6l8 6-8 6z" fill="#111"/></svg></div></div>
  <div class="tile"><div class="tile-photo photo-van" role="img" aria-label="Van with printed vehicle wrap"></div><div class="tile-bar"><span class="tile-small">PRINTED VEHICLE</span><span class="tile-big">WRAP</span><svg class="tile-go" viewBox="0 0 24 24"><circle cx="12" cy="12" r="12" fill="#fff"/><path d="M9 6l8 6-8 6z" fill="#111"/></svg></div></div>
  <div class="tile"><div class="tile-photo photo-car" role="img" aria-label="Two green hatchbacks with tinted windows"></div><div class="tile-bar"><span class="tile-small">WINDOW</span><span class="tile-big">TINT</span><svg class="tile-go" viewBox="0 0 24 24"><circle cx="12" cy="12" r="12" fill="#fff"/><path d="M9 6l8 6-8 6z" fill="#111"/></svg></div></div>
  <div class="tile"><div class="tile-photo photo-car" role="img" aria-label="Two green hatchbacks with tinted headlights"></div><div class="tile-bar"><span class="tile-small">HEADLIGHT</span><span class="tile-big">TINTING</span><svg class="tile-go" viewBox="0 0 24 24"><circle cx="12" cy="12" r="12" fill="#fff"/><path d="M9 6l8 6-8 6z" fill="#111"/></svg></div></div>
  <!-- row 3 -->
  <div class="tile"><div class="tile-photo photo-van" role="img" aria-label="White van with colour change wrap"></div><div class="tile-bar"><span class="tile-small">COLOR CHANGE</span><span class="tile-big">WRAP</span><svg class="tile-go" viewBox="0 0 24 24"><circle cx="12" cy="12" r="12" fill="#fff"/><path d="M9 6l8 6-8 6z" fill="#111"/></svg></div></div>
  <div class="tile"><div class="tile-photo photo-van" role="img" aria-label="Van with printed vehicle wrap"></div><div class="tile-bar"><span class="tile-small">PRINTED VEHICLE</span><span class="tile-big">WRAP</span><svg class="tile-go" viewBox="0 0 24 24"><circle cx="12" cy="12" r="12" fill="#fff"/><path d="M9 6l8 6-8 6z" fill="#111"/></svg></div></div>
  <div class="tile"><div class="tile-photo photo-car" role="img" aria-label="Two green hatchbacks with tinted windows"></div><div class="tile-bar"><span class="tile-small">WINDOW</span><span class="tile-big">TINT</span><svg class="tile-go" viewBox="0 0 24 24"><circle cx="12" cy="12" r="12" fill="#fff"/><path d="M9 6l8 6-8 6z" fill="#111"/></svg></div></div>
  <div class="tile"><div class="tile-photo photo-car" role="img" aria-label="Two green hatchbacks with tinted headlights"></div><div class="tile-bar"><span class="tile-small">HEADLIGHT</span><span class="tile-big">TINTING</span><svg class="tile-go" viewBox="0 0 24 24"><circle cx="12" cy="12" r="12" fill="#fff"/><path d="M9 6l8 6-8 6z" fill="#111"/></svg></div></div>
</main>

<section class="search-band">
  <span class="search-lead">...Or Search &amp; &amp; Save in Seconds!</span>
  <span class="search-label">SEARCH WITHIN</span>
  <span class="search-field">Enter Miles</span>
  <span class="search-label" style="margin-left:10px">OF</span>
  <span class="search-field wide"></span>
  <span class="search-button">SEARCH</span>
</section>

<section>
  <h2 class="help-title" style="font-weight:400">How Can We Help You?</h2>
  <ul class="help-list">
    <li>Text will input here place holder</li>
    <li>Text will input here place holder</li>
    <li>Text will input here place holder</li>
  </ul>
  <div class="compare compare-before">
    <div class="compare-photo" role="img" aria-label="Silver saloon car before window tint"></div>
    <div class="compare-label">BEFORE</div>
  </div>
  <div class="compare compare-after">
    <div class="compare-photo" role="img" aria-label="Silver saloon car after window tint"></div>
    <div class="compare-tag"><span>WINDOW</span><strong>TINT</strong></div>
    <div class="compare-label">AFTER</div>
  </div>
</section>

<div class="footer-bar"></div>
</body>
</html>
```